Redesign of a Restaurant web presence

We need a new design of our restaurant web page which can also be based on a new CI (current main colours are gold, green and pink/violett), urban jungle style.
WORDPRESS is being used for coding the website and there should be no monthly paid plug-ins be used.
Main features should be the presentation of our location, downloadable menus (pdf), a possibility for online reservations (pop-up on start page) and recruitung staff (job descriptions to be viewed).
Focus should be on the design, functionality is very basic.
Multi language preferred (SK,DE,EN).
Working on desktop and mobile devices.
A reference site is fernloft.at
Current page tovimarlund.sk
If the co-operation is good, we also need template layouts for our new printed menu based on the (new) CI.

```html
<!DOCTYPE html>
<html lang="en">
<head>
<meta charset="utf-8">
<title>Tovi Marlund – Café &amp; Restaurant</title>
<link href="https://fonts.googleapis.com/css2?family=Bebas+Neue&family=Poppins:ital,wght@0,400;0,500;1,400&family=Libre+Baskerville&family=Kaushan+Script&display=swap" rel="stylesheet">
<style>
:root{
  --teal:#0d6b6e;
  --gold:#d6a31c;
  --gold-dark:#9c7a1e;
  --green:#0f8f3c;
  --brown:#3b3130;
  --ink:#2b2b2b;
  --white:#ffffff;
  --yellow:#f3d22b;
}
*{box-sizing:border-box;margin:0;padding:0}
html,body{width:1200px;height:4975px;overflow:hidden;background:var(--white)}
body{position:relative;font-family:"Poppins",sans-serif;color:var(--ink)}
.abs{position:absolute}
.display{font-family:"Bebas Neue",sans-serif;line-height:.9;letter-spacing:1px;font-weight:400}
.serif{font-family:"Libre Baskerville",serif}
.script{font-family:"Kaushan Script",cursive}
.ph{position:absolute}

/* header */
.header{top:0;left:0;width:1200px;height:113px;background:var(--white)}
.header .meta{font-size:10px;top:31px}
.header .nav{font-size:12px;top:68px}
.rule{height:1px;background:#d8d8d8;top:56px}
.wordmark{left:600px;top:38px;transform:translateX(-50%);font-family:"Poppins",sans-serif;font-weight:500;font-size:24px;letter-spacing:1px;color:var(--ink);white-space:nowrap}
.soc{width:22px;height:22px;border-radius:50%;background:#e3e3e3;top:17px}

/* hero */
.hero{top:113px;left:0;width:1200px;height:547px;background:var(--teal);overflow:hidden}
.hero h1{left:638px;top:134px;font-size:78px;color:var(--white)}
.eyebrow{left:640px;top:108px;font-size:10px;letter-spacing:5px;color:var(--white)}
.btn{border:3px solid var(--gold);color:var(--white);font-family:"Bebas Neue",sans-serif;font-size:20px;display:flex;align-items:center;justify-content:center;gap:8px}
.btn.light{border-color:var(--white)}
.dot{width:14px;height:14px;border-radius:50%;background:var(--white);top:474px}

/* booking band */
.booking{top:660px;left:0;width:1200px;height:333px;background:var(--gold)}
.wave{position:absolute;left:0;width:1200px;height:14px}
.promo{border:3px dashed var(--white);width:421px;height:181px;display:flex;align-items:center;justify-content:center;text-align:center}
.promo p{font-family:"Bebas Neue",sans-serif;font-size:76px;line-height:.88;color:var(--white)}
.promo .off{color:var(--yellow)}
.field{background:var(--white);font-size:9px;color:#999;padding:10px 12px}
.form-title{font-size:18px;color:var(--white);left:690px;top:48px}

/* explore menu */
.menu-box{left:110px;top:1119px;width:982px;height:442px;background:var(--teal)}
.menu-title{left:268px;top:1200px;font-size:142px;color:var(--white);line-height:.92}

/* features */
.market{right:725px;top:1628px;text-align:right;font-size:58px;color:var(--ink)}
.shield{width:92px;height:101px;top:1632px}
.feat-label{width:140px;text-align:center;top:1748px;font-family:"Bebas Neue",sans-serif;font-size:17px;line-height:1}

/* explore more */
.section-title{left:0;width:1200px;text-align:center;top:1888px;font-size:60px;color:var(--ink)}
.card{left:85px;width:1028px;height:329px;overflow:visible}
.card h3{font-family:"Bebas Neue",sans-serif;font-size:56px;font-weight:400;color:var(--white)}
.card p{font-size:17px;line-height:1.3;color:var(--white);width:370px}

/* newsletter */
.news{top:3285px;left:0;width:1200px;height:392px;background:var(--brown)}
.news .note{left:686px;top:130px;font-size:24px;color:var(--white);line-height:1.4}
.testi{top:3677px;left:0;width:1200px;height:573px;background:linear-gradient(180deg,#2b2624,#4a3a33 60%,#2b2624)}
.quote{left:0;width:1200px;text-align:center;top:3615px;font-family:"Libre Baskerville",serif;font-size:300px;color:var(--yellow);line-height:1}
.testi-text{left:150px;width:900px;text-align:center;top:3886px;font-style:italic;font-size:28px;line-height:1.25;color:var(--white)}

/* connect */
.connect{left:183px;top:4335px;font-size:64px;color:var(--ink)}
.gold-band{top:4666px;left:0;width:1200px;height:222px;background:var(--gold)}
.tile{top:4540px;width:257px;height:255px}
.footer{top:4888px;left:0;width:1200px;height:87px;background:var(--gold-dark);color:var(--white)}
.footer .f{top:40px;font-size:12px;font-family:"Libre Baskerville",serif}
.footer .wordmark-small{left:130px;top:33px;font-family:"Poppins",sans-serif;font-weight:500;font-size:17px;letter-spacing:1px;color:var(--white)}
</style>
</head>
<body>

<header class="header abs">
  <span class="abs meta serif" style="left:129px">info@tovimarlund.sk</span>
  <span class="abs meta serif" style="left:270px">+421 900 123 456</span>
  <div class="abs rule" style="left:129px;width:300px"></div>
  <div class="abs rule" style="left:771px;width:300px"></div>
  <nav>
    <span class="abs nav serif" style="left:129px">Introduction</span>
    <span class="abs nav serif" style="left:245px">Daily Menu</span>
    <span class="abs nav serif" style="left:356px">Our Offer ⌄</span>
    <span class="abs nav serif" style="left:794px">Events ⌄</span>
    <span class="abs nav serif" style="left:885px">Reservation</span>
    <span class="abs nav serif" style="left:1018px">Contacts</span>
  </nav>
  <div class="abs wordmark">TOVI MARLUND</div>
  <span class="abs soc" style="left:877px"></span>
  <span class="abs soc" style="left:907px"></span>
  <span class="abs soc" style="left:937px"></span>
  <span class="abs soc" style="left:967px"></span>
  <svg class="abs" style="left:1011px;top:17px" width="22" height="22" viewBox="0 0 22 22" fill="none" stroke="#2b2b2b" stroke-width="2"><path d="M3 7h16l-2 11H5z"/><path d="M8 7V4h6v3"/></svg>
  <svg class="abs" style="left:1044px;top:17px" width="22" height="22" viewBox="0 0 22 22" fill="none" stroke="#2b2b2b" stroke-width="2"><circle cx="11" cy="11" r="9"/><circle cx="11" cy="9" r="3"/><path d="M5 17c2-3 10-3 12 0"/></svg>
</header>

<section class="hero abs">
  <div class="ph" role="img" aria-label="Tropical palm leaves along the left edge" style="left:0;top:40px;width:200px;height:507px;background:linear-gradient(90deg,#1f7a55,#0d6b6e)"></div>
  <div class="ph" role="img" aria-label="Tropical palm leaves along the right edge" style="left:1070px;top:160px;width:130px;height:387px;background:linear-gradient(270deg,#2b8a5f,#0d6b6e)"></div>
  <div class="ph" role="img" aria-label="Golden bird head sculpture mounted on a dark teal wall panel" style="left:342px;top:32px;width:131px;height:458px;background:linear-gradient(180deg,#0a4a4c,#083d3f)"></div>
  <span class="abs eyebrow">WE BRING THE</span>
  <h1 class="abs display">EXPERIENCE OF<br>FOOD &amp; A GREAT<br>ATMOSPHERE</h1>
  <span class="abs btn" style="left:647px;top:366px;width:184px;height:56px">› JOIN THE TEAM</span>
  <span class="abs dot" style="left:566px"></span>
  <span class="abs dot" style="left:593px;background:var(--yellow)"></span>
  <span class="abs dot" style="left:617px"></span>
</section>

<section class="booking abs">
  <svg class="wave" style="top:-12px" viewBox="0 0 1200 14" preserveAspectRatio="none"><defs><pattern id="w1" width="24" height="14" patternUnits="userSpaceOnUse"><path d="M0 14 Q6 2 12 8 T24 6 V14z" fill="#d6a31c"/></pattern></defs><rect width="1200" height="14" fill="url(#w1)"/></svg>
  <div class="ph" role="img" aria-label="Banana leaf in the lower left corner" style="left:0;top:150px;width:240px;height:183px;background:linear-gradient(45deg,#1d7a4b,#d6a31c)"></div>
  <div class="abs promo" style="left:143px;top:63px"><p>GET <span class="off">$ 5% OFF</span><br>LIMITED-TIME</p></div>
  <span class="abs form-title script">Book A Pleasant Experience With Us</span>
  <div class="abs field" style="left:610px;top:88px;width:223px;height:36px">Name</div>
  <div class="abs field" style="left:846px;top:88px;width:222px;height:36px">Phone</div>
  <div class="abs field" style="left:610px;top:130px;width:223px;height:37px">Email</div>
  <div class="abs field" style="left:846px;top:130px;width:222px;height:37px">Date</div>
  <div class="abs field" style="left:610px;top:177px;width:458px;height:56px">Message</div>
  <span class="abs btn light" style="left:784px;top:248px;width:111px;height:33px;font-size:13px">SEND NOW</span>
</section>

<div class="abs menu-box"></div>
<div class="ph" role="img" aria-label="Smiling woman holding a bowl of fresh salad" style="left:68px;top:1024px;width:318px;height:537px;background:linear-gradient(180deg,#c9a48a,#f2efea 45%,#e9e5df)"></div>
<div class="abs menu-title display">EXPLORE OUR<br>DAILY MENU</div>
<svg class="abs" style="left:541px;top:1296px" width="112" height="112" viewBox="0 0 112 112"><circle cx="56" cy="56" r="54" fill="#0d6b6e"/><path d="M56 32v48M32 56h48" stroke="#fff" stroke-width="9"/></svg>

<div class="abs market display">1<sup style="font-size:22px">ST</sup> ON<br>THE MARKET</div>
<span class="abs display" style="left:392px;top:1772px;font-size:20px;border-bottom:2px solid var(--gold)">ORDER NOW</span>
<svg class="abs shield" style="left:570px" viewBox="0 0 92 101"><path d="M0 0h92v70q0 12-14 18L46 101 14 88Q0 82 0 70z" fill="#0d6b6e"/><path d="M46 66 28 48a11 11 0 0 1 18-13 11 11 0 0 1 18 13z" fill="none" stroke="#fff" stroke-width="4"/></svg>
<svg class="abs shield" style="left:713px" viewBox="0 0 92 101"><path d="M0 0h92v70q0 12-14 18L46 101 14 88Q0 82 0 70z" fill="#0d6b6e"/><circle cx="46" cy="46" r="19" fill="none" stroke="#fff" stroke-width="4"/><path d="M37 46l7 7 12-13" fill="none" stroke="#fff" stroke-width="4"/></svg>
<svg class="abs shield" style="left:858px" viewBox="0 0 92 101"><path d="M0 0h92v70q0 12-14 18L46 101 14 88Q0 82 0 70z" fill="#0d6b6e"/><circle cx="46" cy="40" r="16" fill="none" stroke="#fff" stroke-width="3"/><circle cx="46" cy="40" r="9" fill="none" stroke="#fff" stroke-width="2"/><path d="M36 53l-6 16 8-3 4 7 4-12 4 12 4-7 8 3-6-16" fill="none" stroke="#fff" stroke-width="2.5"/></svg>
<span class="abs feat-label" style="left:546px">PEACEFUL<br>ATMOSPHERE</span>
<span class="abs feat-label" style="left:689px">FRESHNESS OF<br>THE INGREDIENTS</span>
<span class="abs feat-label" style="left:834px">TOVI'S<br>KNOW-HOW</span>

<h2 class="abs section-title display">EXPLORE MORE</h2>

<section class="card abs" style="top:2054px;background:var(--gold)">
  <svg class="wave" style="top:-12px;width:1028px" viewBox="0 0 1028 14" preserveAspectRatio="none"><defs><pattern id="w2" width="24" height="14" patternUnits="userSpaceOnUse"><path d="M0 14 Q6 2 12 8 T24 6 V14z" fill="#d6a31c"/></pattern></defs><rect width="1028" height="14" fill="url(#w2)"/></svg>
  <div class="ph" role="img" aria-label="Clipboard with blank paper surrounded by kitchen utensils and vegetables" style="left:89px;top:-99px;width:406px;height:428px;background:linear-gradient(160deg,#b88a3c,#ece6d6 50%,#4f7a2e)"></div>
  <h3 class="abs" style="left:593px;top:52px">DAILY MENU</h3>
  <p class="abs" style="left:593px;top:120px">Every day a varied menu of dishes made from fresh ingredients. Everyone chooses and enjoys.</p>
  <span class="abs btn light" style="left:595px;top:213px;width:192px;height:56px">› DOWNLOAD NOW</span>
</section>

<section class="card abs" style="top:2438px;background:var(--green)">
  <svg class="wave" style="top:-12px;width:1028px" viewBox="0 0 1028 14" preserveAspectRatio="none"><defs><pattern id="w3" width="24" height="14" patternUnits="userSpaceOnUse"><path d="M0 14 Q6 2 12 8 T24 6 V14z" fill="#0f8f3c"/></pattern></defs><rect width="1028" height="14" fill="url(#w3)"/></svg>
  <div class="ph" role="img" aria-label="Plate of roast chicken on saffron rice with almonds" style="left:581px;top:-33px;width:339px;height:339px;border-radius:50%;background:radial-gradient(circle,#e0a040,#c46a24 55%,#2a2a2a 70%)"></div>
  <h3 class="abs" style="left:166px;top:62px">OUR OFFER</h3>
  <p class="abs" style="left:166px;top:130px">Culinary gems, Slovak specialties and gastronomic experiences from different corners of the world.</p>
  <span class="abs btn" style="left:166px;top:225px;width:162px;height:56px">› ORDER NOW</span>
</section>

<section class="card abs" style="top:2817px;background:var(--teal)">
  <svg class="wave" style="top:-12px;width:1028px" viewBox="0 0 1028 14" preserveAspectRatio="none"><defs><pattern id="w4" width="24" height="14" patternUnits="userSpaceOnUse"><path d="M0 14 Q6 2 12 8 T24 6 V14z" fill="#0d6b6e"/></pattern></defs><rect width="1028" height="14" fill="url(#w4)"/></svg>
  <div class="ph" role="img" aria-label="Platter of grilled meat surrounded by bowls of fruit and side dishes" style="left:89px;top:-33px;width:376px;height:346px;border-radius:45%;background:radial-gradient(circle,#7a3b1e,#c8803a 55%,#0d6b6e 75%)"></div>
  <h3 class="abs" style="left:568px;top:60px">EVENTS</h3>
  <p class="abs" style="left:568px;top:128px">Culinary gems, Slovak specialties and gastronomic experiences from different corners of the world.</p>
  <span class="abs btn" style="left:570px;top:222px;width:162px;height:56px">› ORDER NOW</span>
</section>

<section class="news abs">
  <svg class="wave" style="top:-12px" viewBox="0 0 1200 14" preserveAspectRatio="none"><defs><pattern id="w5" width="24" height="14" patternUnits="userSpaceOnUse"><path d="M0 14 Q6 2 12 8 T24 6 V14z" fill="#3b3130"/></pattern></defs><rect width="1200" height="14" fill="url(#w5)"/></svg>
  <div class="ph" role="img" aria-label="Banana leaf on the left edge" style="left:0;top:200px;width:240px;height:192px;background:linear-gradient(45deg,#1d7a4b,#3b3130)"></div>
  <div class="abs promo" style="left:143px;top:125px"><p>GET <span class="off">$ 5% OFF</span><br>LIMITED-TIME</p></div>
  <p class="abs note script">- Join our email list for this exclusive<br>offer sent directly to your inbox</p>
  <div class="abs field" style="left:666px;top:239px;width:296px;height:37px">Email...</div>
  <span class="abs btn" style="left:983px;top:239px;width:72px;height:37px;font-size:14px">SEND</span>
</section>

<section class="testi abs" role="img" aria-label="Restaurant interior with bar shelves, teal seating and pink armchairs"></section>
<div class="abs quote">“</div>
<p class="abs testi-text">On your walks in Devínská Nova Vsa and its surroundings, you will certainly be attracted by its diversity, natural and cultural wealth. We recommend visiting these places and ways to make yourself or your family a pleasant experience.</p>
<span class="abs" style="left:0;width:1200px;text-align:center;top:4056px;color:var(--yellow);font-size:22px;letter-spacing:2px">★★★★★</span>
<svg class="abs" style="left:98px;top:3935px" width="16" height="24" viewBox="0 0 16 24"><path d="M12 2 3 12l9 10" fill="none" stroke="#fff" stroke-width="2"/></svg>
<svg class="abs" style="left:1086px;top:3935px" width="16" height="24" viewBox="0 0 16 24"><path d="M4 2l9 10-9 10" fill="none" stroke="#fff" stroke-width="2"/></svg>

<h2 class="abs connect display">CONNECT<br>WITH US</h2>
<span class="abs script" style="left:454px;top:4418px;font-size:17px;line-height:1.3">Follow Us<br>On Instagram</span>
<svg class="abs" style="left:420px;top:4438px" width="26" height="50" viewBox="0 0 26 50"><path d="M22 2C4 10 2 30 12 46M6 38l6 8 6-7" fill="none" stroke="#2b2b2b" stroke-width="2"/></svg>
<span class="abs soc" style="left:899px;top:4481px;width:34px;height:34px"></span>
<span class="abs soc" style="left:941px;top:4481px;width:34px;height:34px"></span>
<span class="abs soc" style="left:983px;top:4481px;width:34px;height:34px"></span>
<span class="abs soc" style="left:1025px;top:4481px;width:34px;height:34px"></span>
<div class="abs gold-band"></div>
<div class="ph tile" role="img" aria-label="Wooden dining table with gold leaf wall" style="left:85px;background:linear-gradient(160deg,#c8a060,#7a5a3a)"></div>
<div class="ph tile" role="img" aria-label="Restaurant bar with teal chairs" style="left:342px;background:linear-gradient(180deg,#c9b79a,#1f5a60)"></div>
<div class="ph tile" role="img" aria-label="Table set with glasses and plates" style="left:599px;background:linear-gradient(160deg,#b8323c,#3a2a2a)"></div>
<div class="ph tile" role="img" aria-label="Golden animal sculpture beside teal chairs" style="left:856px;background:linear-gradient(160deg,#2f6f88,#c99a30)"></div>

<footer class="footer abs">
  <span class="abs wordmark-small">TOVI MARLUND</span>
  <span class="abs f" style="left:347px">Introduction</span>
  <span class="abs f" style="left:437px">Daily Menu</span>
  <span class="abs f" style="left:524px">Our Offer</span>
  <span class="abs f" style="left:598px">Events</span>
  <span class="abs f" style="left:665px">Reservation</span>
  <span class="abs f" style="left:772px">Contacts</span>
  <span class="abs f" style="left:888px">Copyright ©2024 tovimarlund</span>
</footer>

</body>
</html>
```